Personal Injury Lawyer Billboard

I would like a design created featuring the image of the lawyer centered in the middle of the design.
To the left of the lawyer's image it should read "INJURED?"
To the right of the lawyer's image, it should read "CALL BRUNO!"
Under Call Bruno, include the phone number 318-555-0187.
At the bottom of the design include the lawyers information "Bruno Pemberly Accident & Injury Lawyers"
PLEASE REMOVED THE BACKGROUND IMAGERY OF THE PHOTO SUBMITTED. Also, the colors for this design should match the colors shown in the logo (navy, white and relective soft gold). Please use those color combinations in ways that best stand out.

```html
<!DOCTYPE html>
<html lang="en">
<head>
<meta charset="utf-8">
<title>Bruno Pemberly Accident &amp; Injury Lawyers – Billboard</title>
<link rel="stylesheet" href="https://fonts.googleapis.com/css2?family=Cinzel:wght@400;500&family=Tinos:wght@400;700&display=swap">
<style>
  :root {
    --navy: #0a1c44;
    --gold: #c9a23b;
    --gold-soft: #d4ac45;
    --white: #ffffff;
    --backdrop: #e9ebef;
    --portrait-top: #2a3b66;
    --portrait-bottom: #14244d;
  }
  * { margin: 0; padding: 0; box-sizing: border-box; }
  html, body {
    width: 1200px;
    height: 879px;
    overflow: hidden;
    background: var(--backdrop);
  }
  .billboard {
    position: absolute;
    left: 0;
    top: 205px;
    width: 1200px;
    height: 470px;
    background: var(--navy);
    overflow: hidden;
  }
  .gold-band {
    position: absolute;
    left: 0;
    top: 390px;
    width: 1200px;
    height: 72px;
    background: var(--gold);
  }
  .headline {
    position: absolute;
    left: 26px;
    top: 162px;
    font-family: "Cinzel", serif;
    font-weight: 400;
    font-size: 84px;
    letter-spacing: 4px;
    line-height: 1;
    color: var(--gold-soft);
  }
  .firm-block {
    position: absolute;
    z-index: 2;
    left: 14px;
    top: 318px;
    width: 424px;
    height: 152px;
    background: var(--navy);
    padding: 6px 0 0 8px;
  }
  .firm-name {
    font-family: "Tinos", serif;
    font-weight: 700;
    font-size: 74px;
    line-height: 68px;
    letter-spacing: -1px;
    color: var(--white);
    white-space: nowrap;
    transform: scaleX(0.58);
    transform-origin: left center;
  }
  .firm-rule {
    height: 2px;
    width: 416px;
    background: var(--white);
    margin-top: 6px;
  }
  .firm-tagline {
    font-family: "Tinos", serif;
    font-weight: 400;
    font-size: 29px;
    line-height: 44px;
    color: var(--white);
    white-space: nowrap;
    transform: scaleX(0.93);
    transform-origin: left center;
  }
  .firm-rule--bottom { margin-top: 2px; }
  .portrait {
    position: absolute;
    z-index: 1;
    left: 450px;
    top: 20px;
    width: 340px;
    height: 450px;
    border-radius: 120px 120px 0 0;
    background: linear-gradient(180deg, var(--portrait-top), var(--portrait-bottom));
  }
  .cta {
    position: absolute;
    left: 824px;
    top: 180px;
    font-family: "Cinzel", serif;
  }
  .cta-line {
    font-weight: 400;
    font-size: 52px;
    line-height: 1;
    letter-spacing: 1px;
    color: var(--gold-soft);
    white-space: nowrap;
  }
  .cta-phone {
    display: flex;
    align-items: center;
    gap: 14px;
    margin-top: 16px;
    font-size: 44px;
    line-height: 1;
    color: var(--gold-soft);
  }
  .cta-phone svg { width: 46px; height: 46px; flex: none; }
</style>
</head>
<body>
  <section class="billboard">
    <div class="gold-band"></div>

    <h1 class="headline">INJURED</h1>

    <div class="portrait" role="img" aria-label="Cut-out portrait of the smiling lawyer in a navy suit and green tie, raising a fist"></div>

    <div class="firm-block">
      <div class="firm-name">BRUNO PEMBERLY</div>
      <div class="firm-rule"></div>
      <div class="firm-tagline">ACCIDENT &amp; INJURY LAWYERS</div>
      <div class="firm-rule firm-rule--bottom"></div>
    </div>

    <div class="cta">
      <div class="cta-line">CALL BRUNO</div>
      <div class="cta-phone">
        <svg viewBox="0 0 46 46" aria-hidden="true">
          <circle cx="23" cy="23" r="20.5" fill="none" stroke="currentColor" stroke-width="3"/>
          <path d="M15.5 12.5c1-.9 2.4-.8 3.2.2l2.2 3c.7 1 .6 2.3-.3 3.1l-1.5 1.3c1.2 2.6 3.2 4.7 5.8 6l1.4-1.5c.8-.9 2.2-1 3.1-.3l3 2.2c1 .8 1.1 2.3.2 3.2l-1.7 1.8c-1.2 1.2-3 1.6-4.6 1-6-2.3-10.6-6.9-12.8-12.9-.6-1.6-.2-3.4 1-4.6z" fill="currentColor"/>
          <path d="M25 13.5a7.5 7.5 0 0 1 7.5 7.5M25 9.5a11.5 11.5 0 0 1 11.5 11.5" fill="none" stroke="currentColor" stroke-width="2" stroke-linecap="round"/>
        </svg>
        <span class="cta-number">318-555-0187</span>
      </div>
    </div>
  </section>
</body>
</html>
```